Business Card for plorvaTEC

Create a Business Card with an existing logo for plorvaTEC AG. We are a Information Technology company that does consulting and developing SW to automate business processes. The main colors are given from the logo.

Industry/Entity Type

Business

Requirements
Nice to have
• we use a a font style Century Gothic in our documents

```html
<!DOCTYPE html>
<html lang="en">
<head>
<meta charset="utf-8">
<title>plorvaTEC AG – Business Card</title>
<link rel="stylesheet" href="https://fonts.googleapis.com/css2?family=Questrial&display=swap">
<style>
  :root {
    --page: #d9d6d2;
    --navy: #053e6f;
    --navy-text: #c9d6e3;
    --paper: #ececec;
    --ink: #3a3a3a;
    --accent: #2f7cc1;
    --mark: #4aa3d8;
  }
  * { box-sizing: border-box; margin: 0; padding: 0; }
  html, body { width: 1200px; height: 900px; overflow: hidden; }
  body {
    background: var(--page);
    font-family: "Questrial", "Century Gothic", sans-serif;
    display: flex;
    flex-direction: column;
    align-items: center;
    justify-content: center;
    gap: 40px;
  }
  .card {
    width: 620px;
    height: 375px;
    position: relative;
    box-shadow: 0 6px 18px rgba(0,0,0,.18);
  }
  /* Front */
  .card--front {
    background: var(--navy);
    display: flex;
    flex-direction: column;
    align-items: center;
    justify-content: center;
    gap: 18px;
  }
  .brand { display: flex; align-items: center; gap: 14px; }
  .brand__dot { width: 46px; height: 46px; border-radius: 50%; background: var(--mark); }
  .card--front .brand__name { color: #ffffff; font-size: 40px; }
  .card--front .web { color: var(--navy-text); font-size: 17px; letter-spacing: 1px; margin-top: 30px; }
  /* Back */
  .card--back {
    background: var(--paper);
    color: var(--ink);
    display: grid;
    grid-template-columns: 250px 1fr;
    padding: 50px 40px 40px 50px;
  }
  .back__brand {
    display: flex;
    flex-direction: column;
    justify-content: flex-end;
    gap: 16px;
    padding-bottom: 30px;
  }
  .back__brand .brand__dot { width: 70px; height: 70px; }
  .back__brand .brand__name { font-size: 44px; color: var(--ink); letter-spacing: -0.5px; }
  .details { display: flex; flex-direction: column; padding-left: 20px; }
  .rule { height: 1px; background: var(--accent); }
  .person { padding: 14px 0 12px; }
  .person__name { font-size: 22px; }
  .person__role { font-size: 15px; margin-top: 2px; }
  .contact { list-style: none; margin-top: 14px; font-size: 14.5px; line-height: 1.45; }
  .contact__label { color: var(--accent); display: inline-block; width: 58px; }
  .address { font-style: normal; font-size: 14.5px; line-height: 1.45; margin-top: 12px; }
  .details .web { color: var(--accent); font-size: 15px; margin-top: 12px; }
</style>
</head>
<body>
  <section class="card card--front" aria-label="Business card front">
    <div class="brand">
      <span class="brand__dot"></span>
      <span class="brand__name">plorvaTEC</span>
    </div>
    <p class="web">www.plorvatec.ch</p>
  </section>

  <section class="card card--back" aria-label="Business card back">
    <div class="back__brand">
      <span class="brand__dot"></span>
      <span class="brand__name">plorvaTEC</span>
    </div>
    <div class="details">
      <div class="rule"></div>
      <div class="person">
        <p class="person__name">Lukas Brenner</p>
        <p class="person__role">CEO</p>
      </div>
      <div class="rule"></div>
      <ul class="contact">
        <li><span class="contact__label">Phone</span>+41 56 318 40 27</li>
        <li><span class="contact__label">Mobile</span>+41 79 462 85 19</li>
        <li><span class="contact__label">Email</span>lukas.brenner@plorvatec.ch</li>
      </ul>
      <address class="address">Hofackerstrasse 8, 5400 Baden<br>Switzerland</address>
      <p class="web">www.plorvatec.ch</p>
    </div>
  </section>
</body>
</html>
```